emerald card

Belvardi/Gems
Est.1972
We are a direct Importer of Colombian Emeralds, with gem lab certificates KSR,PMB 1.0ct. and over.Gem ID and Country of origin
Hal Belvardi belvo@postwing.example
469 555 0176 www. belvardiline.example
The current web page is being redesigned,please ,Belvardi/Gems is a new company. We specialize in Colombian Emeralds.
Some of the designers used the existing web page and companies and created business cards for the wrong companies.
The blue back ground deign from Sri Lanka is the only card design that has all the correct information.

Target Market(s)

Fine Jewelry

Industry/Entity Type

Business

Contact Information for Business Card

Belvardi/Gems

Font styles to use
Other font styles liked:
• Roman

Requirements
Must have
• Belvardi/Gems Hal Belvardi
P.O.Box 318270 Dallas,Tx.75908 Ph. 469 555 0176 E-Mail:belvo@postwing.example
www.belvardiline.example, Emeralds over 1.0ct. are certified for Country of origin and Gem ID-KSR or PMB cerificates.

We are importers of Colombian Emeralds all Emeralds over 1.0ct.
Dallas,Tx. 75908
KSR,PMB
Nice to have
• Picture of Emerald
Should not have
• No other company names
We are changing information on our web site.do not use the web page for design.

```html
<!DOCTYPE html>
<html lang="en">
<head>
<meta charset="utf-8">
<title>Belvardi/Gems – Business Card</title>
<link href="https://fonts.googleapis.com/css2?family=Cormorant+Garamond:wght@500&family=Open+Sans:wght@400;700&display=swap" rel="stylesheet">
<style>
  :root {
    --stage: #2b2623;
    --card-crimson: #a0122e;
    --card-rose: #b8375a;
    --card-dark: #0d0a0b;
    --gold: #e4b93c;
    --gold-soft: #d9b24a;
    --muted-gold: #c9a24a;
  }
  * { margin: 0; padding: 0; box-sizing: border-box; }
  html, body {
    width: 1200px;
    height: 913px;
    overflow: hidden;
    background: var(--stage);
  }
  .stage {
    position: relative;
    width: 1200px;
    height: 913px;
    display: flex;
    align-items: center;
    justify-content: center;
    gap: 50px;
  }
  .card {
    position: relative;
    width: 520px;
    height: 298px;
    border-radius: 4px;
    overflow: hidden;
    background:
      linear-gradient(150deg, var(--card-crimson) 0%, #6e0f24 30%, #3a1118 55%, var(--card-dark) 100%);
    box-shadow: 0 14px 30px rgba(0,0,0,0.45);
  }
  .card::before {
    content: "";
    position: absolute;
    inset: 0;
    background: linear-gradient(200deg, rgba(184,55,90,0.7) 0%, rgba(184,55,90,0) 45%);
  }
  .brand {
    position: absolute;
    display: flex;
    align-items: center;
    gap: 12px;
    font-family: "Cormorant Garamond", "Times New Roman", serif;
    font-weight: 500;
    color: var(--gold);
    white-space: nowrap;
  }
  .brand-mark {
    width: 12px;
    height: 12px;
    background: var(--gold);
  }
  .card-front .brand {
    left: 50%;
    top: 108px;
    transform: translateX(-50%);
    font-size: 48px;
  }
  .front-tagline {
    position: absolute;
    left: 0;
    right: 0;
    top: 186px;
    text-align: center;
    font-family: "Open Sans", Arial, sans-serif;
    font-size: 12px;
    line-height: 1.6;
    color: var(--muted-gold);
  }
  .front-rule {
    position: absolute;
    left: 130px;
    right: 130px;
    top: 176px;
    height: 1px;
    background: linear-gradient(90deg, rgba(228,185,60,0), var(--gold), rgba(228,185,60,0));
  }
  .card-back .brand {
    left: 40px;
    top: 52px;
    font-size: 38px;
  }
  .holder {
    position: absolute;
    left: 40px;
    bottom: 42px;
    font-family: "Open Sans", Arial, sans-serif;
  }
  .holder-name {
    font-weight: 700;
    font-size: 18px;
    color: var(--gold);
  }
  .holder-title {
    font-size: 13px;
    color: var(--muted-gold);
    margin-top: 2px;
    padding-left: 32px;
  }
  .contact {
    position: absolute;
    right: 30px;
    top: 128px;
    list-style: none;
    font-family: "Open Sans", Arial, sans-serif;
    font-size: 13px;
    color: var(--gold-soft);
  }
  .contact li {
    display: flex;
    align-items: center;
    gap: 10px;
    margin-bottom: 6px;
    white-space: nowrap;
  }
  .contact svg {
    width: 14px;
    height: 14px;
    fill: var(--gold-soft);
    flex: none;
  }
</style>
</head>
<body>
  <main class="stage">
    <section class="card card-front" aria-label="Card front">
      <div class="brand"><span class="brand-mark"></span>Belvardi/Gems</div>
      <div class="front-rule"></div>
      <p class="front-tagline">
        Est. 1972 · Direct Importer of Colombian Emeralds<br>
        KSR, PMB certified 1.0ct. and over · Gem ID &amp; Country of origin
      </p>
    </section>

    <section class="card card-back" aria-label="Card back">
      <div class="brand"><span class="brand-mark"></span>Belvardi/Gems</div>

      <div class="holder">
        <p class="holder-name">Hal Belvardi</p>
        <p class="holder-title">Owner / Propritor</p>
      </div>

      <ul class="contact">
        <li>
          <svg viewBox="0 0 16 16" aria-hidden="true"><path d="M1 5c0-2 2-3 7-3s7 1 7 3v1h-4V5H5v1H1zM3 7h10l1 7H2zm5 2a2 2 0 100 4 2 2 0 000-4z"/></svg>
          469 555 0176
        </li>
        <li>
          <svg viewBox="0 0 16 16" aria-hidden="true"><path d="M1 3h14v10H1zm1.5 1.2L8 8.6l5.5-4.4z"/></svg>
          belvo@postwing.example
        </li>
        <li>
          <svg viewBox="0 0 16 16" aria-hidden="true"><path d="M8 1a7 7 0 100 14A7 7 0 008 1zm0 1.5c.8 0 1.7 1.5 2 3.8H6c.3-2.3 1.2-3.8 2-3.8zM2.6 6.3h2A14 14 0 004.5 9.7h-2a5.6 5.6 0 01.1-3.4zm8.8 0h2a5.6 5.6 0 010 3.4h-2a14 14 0 000-3.4zM6 9.7a12 12 0 010-3.4h4a12 12 0 010 3.4zm0 1.5h4c-.3 2.3-1.2 3.8-2 3.8s-1.7-1.5-2-3.8z"/></svg>
          www.belvardiline.example
        </li>
        <li>
          <svg viewBox="0 0 16 16" aria-hidden="true"><path d="M8 1a5 5 0 00-5 5c0 4 5 9 5 9s5-5 5-9a5 5 0 00-5-5zm0 3a2 2 0 110 4 2 2 0 010-4z"/></svg>
          P.O.Box 318270 Dallas, Tx. 75908
        </li>
      </ul>
    </section>
  </main>
</body>
</html>
```